Refrigeration & Air Conditioning modern and appealing

We want to design a business card that is modern and appealing using existing logo supplied

Front card
Residential Commercial Diary
RTA : AU071523
Licence L258907

Back card
Marcus Ovenly
Director
0491 352 406
info@frostvalecooling.com.au
www.frostvalecooling.com.au
• Air Conditioning
• Cool Rooms & Refrigeration
• Installation
• Service & Repair
• Preventative Maintenance

We offer 24/7 emergency service

```html
<!DOCTYPE html>
<html lang="en">
<head>
<meta charset="utf-8">
<title>Frostvale Cooling – Business Card</title>
<link href="https://fonts.googleapis.com/css2?family=Montserrat:ital,wght@0,400;0,500;0,700;0,800;1,700&family=Roboto+Condensed:ital,wght@1,700&family=Roboto:wght@400&display=swap" rel="stylesheet">
<style>
  :root{
    --stage:#121212;
    --card:#2a2a2b;
    --white:#f4f4f4;
    --purple:#9a4fe0;
    --purple-light:#c07af2;
    --lilac:#a9b4f0;
    --text-muted:#e6e6e6;
  }
  *{margin:0;padding:0;box-sizing:border-box}
  html,body{width:1200px;height:963px;overflow:hidden;background:var(--stage)}
  .stage{width:1200px;height:963px;display:flex;flex-direction:column;align-items:center;justify-content:center;gap:40px}
  .card{position:relative;width:760px;height:434px;background:var(--card);border-radius:4px;box-shadow:0 14px 34px rgba(0,0,0,.6);overflow:hidden;color:var(--white);font-family:"Montserrat",sans-serif}

  .brand{display:flex;align-items:center;gap:14px}
  .brand-dot{width:34px;height:34px;border-radius:50%;background:var(--purple)}
  .brand-name{font-family:"Montserrat",sans-serif;font-weight:800;font-size:44px;letter-spacing:1px;color:var(--white);text-transform:uppercase}

  /* contact side */
  .contact .brand{position:absolute;left:60px;top:46px}
  .person{position:absolute;left:60px;top:150px;padding-left:22px;border-left:8px solid var(--purple)}
  .person-name{font-family:"Roboto Condensed",sans-serif;font-style:italic;font-weight:700;font-size:30px;text-transform:uppercase;color:var(--purple-light);line-height:1}
  .person-role{font-family:"Roboto",sans-serif;font-size:20px;margin-top:6px}
  .details{position:absolute;left:60px;top:250px;list-style:none;font-family:"Roboto",sans-serif;font-size:19px;line-height:1.55}
  .details li{display:flex;align-items:center;gap:12px}
  .details svg{width:18px;height:18px;fill:var(--purple-light)}
  .licence{margin-top:4px}
  .licence .label{color:var(--purple-light)}

  /* services side */
  .services .brand{position:absolute;left:170px;top:40px}
  .sectors{position:absolute;left:170px;top:112px;font-weight:700;font-size:24px;color:var(--purple-light)}
  .service-list{position:absolute;left:185px;top:158px;list-style:none;font-weight:500;font-size:21px;line-height:1.42}
  .service-list li::before{content:"";display:inline-block;width:9px;height:9px;border-radius:50%;background:var(--purple-light);margin-right:12px;vertical-align:middle}
  .offer{position:absolute;left:110px;top:340px;display:flex;align-items:center;gap:14px}
  .offer-lead{font-weight:800;font-size:20px;text-transform:uppercase}
  .badge{width:70px;height:70px}
  .offer-text{font-weight:800;font-size:20px;line-height:1.1;text-transform:uppercase}
  .offer-text .accent{color:var(--purple-light)}
</style>
</head>
<body>
<main class="stage">

  <section class="card contact">
    <div class="brand">
      <span class="brand-dot"></span>
      <span class="brand-name">Frostvale</span>
    </div>
    <div class="person">
      <p class="person-name">Marcus Ovenly</p>
      <p class="person-role">Director</p>
    </div>
    <ul class="details">
      <li><svg viewBox="0 0 24 24"><path d="M6.6 10.8a15.1 15.1 0 0 0 6.6 6.6l2.2-2.2c.3-.3.7-.4 1-.2 1.1.4 2.3.6 3.6.6.6 0 1 .4 1 1V20c0 .6-.4 1-1 1A17 17 0 0 1 3 4c0-.6.4-1 1-1h3.5c.6 0 1 .4 1 1 0 1.3.2 2.5.6 3.6.1.3 0 .7-.2 1z"/></svg>0491 352 406</li>
      <li><svg viewBox="0 0 24 24"><path d="M2 5h20v14H2zm2 2v.5l8 5 8-5V7l-8 5z"/></svg>info@frostvalecooling.com.au</li>
      <li><svg viewBox="0 0 24 24"><path d="M12 2a10 10 0 1 0 0 20 10 10 0 0 0 0-20zm0 2c.9 1.2 1.6 2.6 2 4h-4c.4-1.4 1.1-2.8 2-4zM4.3 14a8 8 0 0 1 0-4h3.5a16 16 0 0 0 0 4zm5.7 0a14 14 0 0 1 0-4h4a14 14 0 0 1 0 4zm6.2 0a16 16 0 0 0 0-4h3.5a8 8 0 0 1 0 4z"/></svg>www.frostvalecooling.com.au</li>
      <li class="licence"><span class="label">RTA:</span>&nbsp;AU071523 <span class="label">&nbsp;|&nbsp; Licence:</span>&nbsp;L258907</li>
    </ul>
  </section>

  <section class="card services">
    <div class="brand">
      <span class="brand-dot"></span>
      <span class="brand-name">Frostvale</span>
    </div>
    <p class="sectors">Residential Commercial Diary</p>
    <ul class="service-list">
      <li>Air Conditioning</li>
      <li>Cool Rooms &amp; Refrigeration</li>
      <li>Installation</li>
      <li>Service &amp; Repair</li>
      <li>Preventative Maintenance</li>
    </ul>
    <div class="offer">
      <span class="offer-lead">We offer</span>
      <svg class="badge" viewBox="0 0 70 70" aria-hidden="true">
        <path d="M10 42 A26 26 0 1 1 58 22" fill="none" stroke="#9a4fe0" stroke-width="6" stroke-linecap="round"/>
        <path d="M52 14 L64 20 L54 29 Z" fill="#9a4fe0"/>
        <text x="35" y="42" text-anchor="middle" font-family="Montserrat, sans-serif" font-weight="800" font-size="15" fill="#f4f4f4">24/7</text>
      </svg>
      <p class="offer-text">Emergency<br><span class="accent">Service</span></p>
    </div>
  </section>

</main>
</body>
</html>
```